Business Card Design

I need a business card for company that is a limited company that was originally an off-road vehicle company (atv's side by sides snowmobiles and motorcycles) and I have recently sold the assets of the company that was operating under a different name and have become semi retired. I continue to do maintenance on these types of vehicles and also sell and install parts and accessories. Recently I have also contracted to a snowmobile club to operate their groomer to groom the snowmobile trails. I would like bright and bold colors.
Industry/Entity Type
Club
Contact Information for Business Card
KTV Holdings Ltd.
Milo Fenwick
780-413-2769

```html
<!DOCTYPE html>
<html lang="en">
<head>
<meta charset="utf-8">
<title>KTV Holdings Ltd. – Business Card</title>
<link rel="stylesheet" href="https://fonts.googleapis.com/css2?family=Maven+Pro:wght@500;700&family=Varela+Round&display=swap">
<style>
  :root {
    --backdrop: #e4e6e8;
    --card-silver-light: #f6f7f8;
    --card-silver-mid: #e2e4e6;
    --card-white: #fbfbfb;
    --teal: #1fb3b5;
    --teal-dark: #139a9d;
    --quote-mint: #a9d3d4;
    --ink: #2a2c2e;
    --ink-soft: #55585b;
  }
  * { box-sizing: border-box; margin: 0; padding: 0; }
  html, body { width: 1200px; height: 800px; overflow: hidden; }
  body {
    background: var(--backdrop);
    font-family: "Varela Round", "Maven Pro", sans-serif;
    color: var(--ink);
    position: relative;
  }
  .card {
    position: absolute;
    top: 246px;
    width: 540px;
    height: 308px;
    border-radius: 4px;
    box-shadow: 0 6px 18px rgba(0,0,0,0.18);
    overflow: hidden;
  }
  /* Front */
  .card-front {
    left: 40px;
    background: linear-gradient(120deg, var(--card-silver-mid) 0%, var(--card-silver-light) 45%, var(--card-silver-mid) 100%);
  }
  .company-name {
    position: absolute;
    top: 26px;
    left: 30px;
    font-family: "Maven Pro", sans-serif;
    font-weight: 700;
    font-size: 22px;
    color: var(--ink);
    letter-spacing: 0.3px;
  }
  .contact-list {
    position: absolute;
    top: 30px;
    right: 30px;
    list-style: none;
    font-size: 16px;
    color: var(--ink-soft);
  }
  .contact-list li {
    display: flex;
    align-items: center;
    gap: 12px;
    margin-bottom: 12px;
  }
  .contact-list svg { width: 16px; height: 16px; flex: none; }
  .person-name {
    position: absolute;
    top: 142px;
    left: 0;
    width: 100%;
    text-align: center;
    font-family: "Maven Pro", sans-serif;
    font-weight: 500;
    font-size: 38px;
    color: var(--teal);
    letter-spacing: 0.5px;
  }
  .accent-band {
    position: absolute;
    left: 0;
    bottom: 0;
    width: 100%;
    height: 22px;
    background: linear-gradient(90deg, var(--teal-dark), var(--teal));
  }
  /* Back */
  .card-back {
    left: 620px;
    background: var(--card-white);
  }
  .statement {
    position: absolute;
    top: 92px;
    left: 70px;
    right: 40px;
    font-size: 19px;
    line-height: 1.4;
    font-weight: 700;
    color: var(--ink);
    -webkit-text-stroke: 0.35px var(--ink);
  }
  .quote-mark {
    position: absolute;
    font-family: Georgia, serif;
    font-size: 84px;
    line-height: 1;
    color: var(--quote-mint);
    font-weight: 700;
  }
  .quote-open { top: 62px; left: 22px; }
  .quote-close { top: 168px; right: 26px; }
</style>
</head>
<body>
  <section class="card card-front" aria-label="Business card front">
    <div class="company-name">KTV Holdings Ltd.</div>
    <ul class="contact-list">
      <li>
        <svg viewBox="0 0 16 16" aria-hidden="true"><path d="M3.6 1.5l2.2 2.6-1.3 1.6c.9 2 2.4 3.6 4.4 4.5l1.6-1.3 2.6 2.2-1.2 2.2C7.3 13 3 8.7 1.7 2.7z" fill="#55585b"/></svg>
        <span>780-413-2769</span>
      </li>
      <li>
        <svg viewBox="0 0 16 16" aria-hidden="true"><rect x="1" y="3.5" width="14" height="9" fill="none" stroke="#55585b" stroke-width="1.2"/><path d="M1 3.5l7 5.5 7-5.5" fill="none" stroke="#55585b" stroke-width="1.2"/></svg>
        <span>ktvhold.77@gmail.com</span>
      </li>
    </ul>
    <h1 class="person-name">Milo Fenwick</h1>
    <div class="accent-band"></div>
  </section>

  <section class="card card-back" aria-label="Business card back">
    <span class="quote-mark quote-open" aria-hidden="true">&ldquo;</span>
    <p class="statement">I am a journeyman red seal automotive technician journeyman red seal motorcycle technician and journeyman parts man.</p>
    <span class="quote-mark quote-close" aria-hidden="true">&rdquo;</span>
  </section>
</body>
</html>
```